Brisk Mend - Handyman and Home Repair Services

I need a business card/letterhead logo for my new handyman service in my local area. I'm happy for a logo design to be done prior to business card design so it can be incorporated on to the card, for which I'd be happy to pay more for. I'd like it to be modern and not using the typical pictures of tools and cartoon characters in dungarees! I like the idea of tools but in a more modern way i.e subtle background images in different shades to main colour. I do like the american retro designs and those that show age and patina for example, having an image half old, half new in its appearance to represent the repairing of things. Colours in mind are 1950's retro colours, ie using grey with pastel greens, red and cream. I'd like to break the mould and the stigma thats attached to these jobs and make it more cool and up to date. I hope this will attract interior designers and more modern businesses to use my services.

This is the logo design I like and would be happy for this idea and colours:

http://pavo-sunlark.co.uk/wp-content/uploads/2011/01/p-s_logo600px.png

Industry/Entity Type

Handyman

```html
<!DOCTYPE html>
<html lang="en">
<head>
<meta charset="utf-8">
<title>Brisk Mend – Business Cards</title>
<link rel="stylesheet" href="https://fonts.googleapis.com/css2?family=Roboto+Condensed:wght@400;700&display=swap">
<style>
  :root {
    --canvas: #e4e2dc;
    --card-grey: #4a4a4c;
    --card-grey-light: #5a5a5c;
    --lime: #8fd13a;
    --lime-light: #a7e04d;
    --cream: #f3efc4;
    --ink-dark: #1f1f20;
  }
  * { box-sizing: border-box; margin: 0; padding: 0; }
  html, body { width: 1200px; height: 855px; overflow: hidden; }
  body {
    background: var(--canvas);
    font-family: "Roboto Condensed", Arial, sans-serif;
    position: relative;
  }
  .card {
    position: absolute;
    width: 520px;
    height: 300px;
    border-radius: 22px;
    overflow: hidden;
    background: radial-gradient(ellipse at 40% 45%, var(--card-grey-light), var(--card-grey) 70%);
    box-shadow: 0 10px 28px rgba(0,0,0,.25);
  }
  .card--front { left: 60px; top: 200px; }
  .card--back { left: 620px; top: 200px; }

  .tool-backdrop {
    position: absolute;
    left: 90px; top: 40px;
    width: 250px; height: 220px;
    border-radius: 50%;
    background: radial-gradient(circle, rgba(60,60,62,.8), rgba(60,60,62,0) 70%);
  }
  .brand {
    position: absolute;
    display: flex;
    align-items: center;
    gap: 12px;
  }
  .brand__dot {
    width: 18px; height: 18px;
    border-radius: 50%;
    background: var(--lime);
  }
  .brand__name {
    font-weight: 700;
    color: var(--lime);
    text-transform: uppercase;
    letter-spacing: 1px;
  }
  .card--front .brand { left: 110px; top: 118px; }
  .card--front .brand__name { font-size: 46px; }

  .front__stripe {
    position: absolute;
    left: 0; right: 0; bottom: 44px;
    height: 6px;
    background: var(--cream);
  }
  .front__url {
    position: absolute;
    right: 28px; bottom: 58px;
    color: var(--lime);
    font-weight: 700;
    font-size: 22px;
    letter-spacing: 1px;
  }

  .back__band {
    position: absolute;
    left: 0; top: 0; bottom: 0;
    width: 190px;
    background: linear-gradient(160deg, var(--lime-light), var(--lime));
    display: flex;
    align-items: center;
    justify-content: center;
  }
  .back__band .brand { position: static; }
  .back__band .brand__dot { background: var(--ink-dark); }
  .back__band .brand__name { color: var(--ink-dark); font-size: 28px; }

  .back__content {
    position: absolute;
    left: 220px; top: 40px; right: 24px; bottom: 36px;
    display: flex;
    flex-direction: column;
    justify-content: space-between;
  }
  .tagline {
    color: var(--cream);
    font-weight: 700;
    text-transform: uppercase;
    font-size: 25px;
    line-height: 1.15;
    letter-spacing: .5px;
  }
  .contact__name {
    color: var(--lime);
    font-weight: 700;
    text-transform: uppercase;
    font-size: 26px;
    letter-spacing: .5px;
  }
  .contact__phone {
    display: flex;
    align-items: center;
    gap: 10px;
    color: var(--cream);
    font-size: 22px;
    letter-spacing: 1px;
    margin-top: 4px;
  }
  .contact__phone svg { width: 20px; height: 20px; }

  .standalone-brand { left: 110px; top: 620px; }
  .standalone-brand .brand__name { font-size: 40px; }
</style>
</head>
<body>

  <section class="card card--front">
    <div class="tool-backdrop" role="img" aria-label="Faint silhouettes of hand tools behind the logo"></div>
    <div class="brand">
      <span class="brand__dot"></span>
      <span class="brand__name">Brisk Mend</span>
    </div>
    <p class="front__url">WWW.BRISKMEND.CO.UK</p>
    <div class="front__stripe"></div>
  </section>

  <section class="card card--back">
    <div class="back__band">
      <div class="brand">
        <span class="brand__dot"></span>
        <span class="brand__name">Brisk Mend</span>
      </div>
    </div>
    <div class="back__content">
      <p class="tagline">Handyman Services<br>From Repair to Install</p>
      <div class="contact">
        <p class="contact__name">Owen Hartley</p>
        <p class="contact__phone">
          <svg viewBox="0 0 20 20" aria-hidden="true">
            <circle cx="10" cy="10" r="9" fill="var(--lime)"/>
            <rect x="7" y="4.5" width="6" height="11" rx="1.2" fill="none" stroke="var(--ink-dark)" stroke-width="1.4"/>
            <circle cx="10" cy="13.2" r=".8" fill="var(--ink-dark)"/>
          </svg>
          07700 900418
        </p>
      </div>
    </div>
  </section>

  <div class="brand standalone-brand">
    <span class="brand__dot"></span>
    <span class="brand__name">Brisk Mend</span>
  </div>

</body>
</html>
```